Refresh of Business Card Design

Want to refresh the business card design with the new logo while adhering to style guide as attached. Would like to match feel of website www.durmackvinex.com

```html
<!DOCTYPE html>
<html lang="en">
<head>
<meta charset="utf-8">
<title>Durmack Vinex – Business Card</title>
<link rel="stylesheet" href="https://fonts.googleapis.com/css2?family=Open+Sans:wght@400;600;700;800&display=swap">
<style>
  :root {
    --backdrop: #e6e6e4;
    --card: #050607;
    --card-front: #000000;
    --white: #ffffff;
    --red: #e3141d;
    --rule: #bfbfbf;
  }
  * { margin: 0; padding: 0; box-sizing: border-box; }
  html, body { width: 1200px; height: 780px; overflow: hidden; }
  body {
    background: var(--backdrop);
    font-family: "Open Sans", Arial, sans-serif;
    color: var(--white);
  }
  .canvas {
    position: relative;
    width: 1200px;
    height: 780px;
    display: flex;
    align-items: center;
    justify-content: center;
    gap: 40px;
  }
  .card {
    position: relative;
    width: 560px;
    height: 320px;
    background: var(--card);
    box-shadow: 0 6px 18px rgba(0,0,0,.28);
  }
  .card--front { background: var(--card-front); }

  .brand {
    position: absolute;
    display: flex;
    align-items: center;
    white-space: nowrap;
  }
  .brand__dot {
    border-radius: 50%;
    background: var(--red);
    flex: none;
  }
  .brand__name {
    font-weight: 600;
    color: var(--white);
    letter-spacing: .06em;
    text-transform: uppercase;
  }
  .card--front .brand {
    left: 50%; top: 50%;
    transform: translate(-50%, -50%);
    gap: 18px;
  }
  .card--front .brand__dot { width: 46px; height: 46px; }
  .card--front .brand__name { font-size: 30px; }

  .card--back .brand {
    left: 40px; top: 152px;
    gap: 10px;
  }
  .card--back .brand__dot { width: 24px; height: 24px; }
  .card--back .brand__name { font-size: 17px; }

  .divider {
    position: absolute;
    left: 290px; top: 70px;
    width: 1px; height: 150px;
    background: var(--rule);
  }
  .person {
    position: absolute;
    left: 318px; top: 62px;
  }
  .person__name {
    font-size: 28px;
    font-weight: 800;
    line-height: 1;
    letter-spacing: -.01em;
  }
  .person__first { color: var(--red); }
  .person__last { color: var(--white); }
  .person__role {
    margin-top: 6px;
    font-size: 13px;
    font-weight: 600;
  }
  .contacts {
    list-style: none;
    margin-top: 14px;
    font-size: 12px;
  }
  .contacts li {
    display: flex;
    align-items: center;
    gap: 8px;
    height: 22px;
  }
  .contacts svg { width: 12px; height: 12px; flex: none; }
  .address {
    position: absolute;
    left: 200px; top: 246px;
    font-size: 13px;
    line-height: 1.5;
  }
</style>
</head>
<body>
<main class="canvas">
  <section class="card card--front" aria-label="Card front">
    <div class="brand">
      <span class="brand__dot"></span>
      <span class="brand__name">Durmack Vinex</span>
    </div>
  </section>

  <section class="card card--back" aria-label="Card back">
    <div class="brand">
      <span class="brand__dot"></span>
      <span class="brand__name">Durmack Vinex</span>
    </div>

    <span class="divider"></span>

    <div class="person">
      <h1 class="person__name"><span class="person__first">Rowan</span> <span class="person__last">Pellick</span></h1>
      <p class="person__role">Sales</p>
      <ul class="contacts">
        <li>
          <svg viewBox="0 0 24 24" aria-hidden="true"><path fill="#e3141d" d="M6.6 10.8a15.1 15.1 0 0 0 6.6 6.6l2.2-2.2a1 1 0 0 1 1-.25 11.4 11.4 0 0 0 3.6.57 1 1 0 0 1 1 1V20a1 1 0 0 1-1 1A17 17 0 0 1 3 4a1 1 0 0 1 1-1h3.5a1 1 0 0 1 1 1c0 1.25.2 2.45.57 3.57a1 1 0 0 1-.25 1z"/></svg>
          <span>555.014.2290</span>
        </li>
        <li>
          <svg viewBox="0 0 24 24" aria-hidden="true"><circle cx="12" cy="12" r="9" fill="none" stroke="#e3141d" stroke-width="2.4"/><path d="M3 12h18M12 3c3 3.2 3 14.8 0 18M12 3c-3 3.2-3 14.8 0 18" fill="none" stroke="#e3141d" stroke-width="2"/></svg>
          <span>www.durmackvinex.com</span>
        </li>
        <li>
          <svg viewBox="0 0 24 24" aria-hidden="true"><rect x="2" y="5" width="20" height="14" rx="1.5" fill="#e3141d"/><path d="M3 6.5l9 7 9-7" fill="none" stroke="#050607" stroke-width="1.8"/></svg>
          <span>rpellick@durmackvinex.com</span>
        </li>
      </ul>
    </div>

    <address class="address" style="font-style: normal;">
      P.O. Box 40318 Harlow, TX 79802<br>
      72 Linden Ct Bramwell, Texas 79140
    </address>
  </section>
</main>
</body>
</html>
```